Paper Lantern Theory - Podcast Cover

Paper Lantern Theory is a weekly podcast that dispels some of the myths about conventional economic thinking and provides a new way of thinking about issues that are faced by the global economy. It's insightful, thought-provoking and, most importantly, fun. We are refreshing the look and sound of the podcast. I have attached a copy of the old amateur design (which I did!)

Target Market(s)

Male oriented, smart folk with an interest in politics and economics

Font styles to use
Sans Serif

Requirements
Must have
• Clearly visible title, even when reduced in size. Must be 3000 pixels by 3000 pixels.
Nice to have
• This podcast challenges the status quo. It should reflect that. Photos and names of the hosts. Actually, because th ephotos are so different, we'd be open to the idea of a caricature if you can do that within the price.

```html
<!DOCTYPE html>
<html lang="en">
<head>
<meta charset="UTF-8">
<title>Paper Lantern Theory – Podcast Cover</title>
<link rel="stylesheet" href="https://fonts.googleapis.com/css2?family=Poppins:wght@500;700&display=swap">
<style>
  :root {
    --bg: #2a2627;
    --white: #ffffff;
    --red: #dc1f26;
    --ring: #8c8c8c;
    --note-face: #c9bfba;
    --note-shade: #7d7472;
    --note-ink: #3e3a3b;
    --stack-edge: #b5a79d;
    --stack-pink: #c79f9a;
    --stack-green: #5f7158;
    --host-a-bg: #3c3440;
    --host-a-shirt: #e9e6e0;
    --host-b-bg: #e3e4e6;
    --host-b-shirt: #2f8ea6;
  }
  html, body {
    margin: 0;
    padding: 0;
    width: 1200px;
    height: 1200px;
    overflow: hidden;
    background: var(--bg);
  }
  .cover {
    position: relative;
    width: 1200px;
    height: 1200px;
    background: var(--bg);
    overflow: hidden;
    font-family: "Poppins", sans-serif;
    color: var(--white);
  }

  /* banknote photograph area */
  .cover__artwork {
    position: absolute;
    top: 0;
    left: 600px;
    width: 600px;
    height: 1200px;
    background:
      linear-gradient(90deg,
        var(--bg) 0%,
        rgba(42,38,39,0.85) 10%,
        rgba(42,38,39,0.35) 22%,
        rgba(42,38,39,0) 32%),
      linear-gradient(180deg,
        rgba(40,36,37,0.75) 0%,
        rgba(40,36,37,0.15) 18%,
        rgba(40,36,37,0) 40%,
        rgba(40,36,37,0.1) 70%,
        rgba(40,36,37,0.55) 100%),
      linear-gradient(90deg,
        var(--note-shade) 0%,
        var(--note-face) 30%,
        var(--note-face) 60%,
        var(--note-shade) 72%,
        var(--stack-pink) 74%,
        var(--stack-edge) 82%,
        var(--stack-edge) 88%,
        var(--stack-green) 92%,
        var(--note-ink) 100%);
  }

  .cover__title {
    position: absolute;
    left: 76px;
    top: 52px;
    margin: 0;
    font-weight: 700;
    font-size: 126px;
    line-height: 144px;
    letter-spacing: -3px;
  }
  .cover__title span { display: block; }

  .cover__subtitle {
    position: absolute;
    left: 375px;
    top: 624px;
    margin: 0;
    font-weight: 700;
    font-size: 72px;
    line-height: 84px;
    letter-spacing: -1.5px;
  }

  .host {
    position: absolute;
    top: 747px;
    width: 380px;
  }
  .host--left { left: 192px; }
  .host--right { left: 651px; }

  .host__photo {
    display: block;
    width: 272px;
    height: 272px;
    margin: 0 auto;
    border-radius: 50%;
    border: 5px solid var(--ring);
    box-sizing: border-box;
  }
  .host--left .host__photo {
    background: linear-gradient(180deg,
      var(--host-a-bg) 0%, var(--host-a-bg) 62%,
      #8d8888 70%, var(--host-a-shirt) 80%, var(--host-a-shirt) 100%);
  }
  .host--right .host__photo {
    background: linear-gradient(180deg,
      var(--host-b-bg) 0%, var(--host-b-bg) 60%,
      #c99a8c 66%, var(--host-b-shirt) 76%, var(--host-b-shirt) 100%);
  }

  .host__name {
    margin: 31px 0 0;
    height: 69px;
    background: var(--red);
    font-weight: 500;
    font-size: 41px;
    line-height: 71px;
    text-align: center;
    letter-spacing: -0.5px;
  }
</style>
</head>
<body>
  <main class="cover">
    <div class="cover__artwork" role="img" aria-label="Close-up photograph of a rolled stack of banknotes held with red rubber bands"></div>

    <h1 class="cover__title">
      <span>The Paper</span>
      <span>Lantern</span>
      <span>Theory</span>
    </h1>

    <p class="cover__subtitle">Podcast with</p>

    <section class="host host--left">
      <div class="host__photo" role="img" aria-label="Portrait photo of host ProfAlanReed in a white T-shirt against a dark wall"></div>
      <p class="host__name">ProfAlanReed</p>
    </section>

    <section class="host host--right">
      <div class="host__photo" role="img" aria-label="Portrait photo of host Martinvoss in a teal polo shirt against a light wall"></div>
      <p class="host__name">Martinvoss</p>
    </section>
  </main>
</body>
</html>
```